We are full service plumbing contractors that are capable of performing all of your plumbing need...

A clean, crisp website that conveys we can handle any plumbing from drain cleaning, repairs, to new construction. But emphasis on Leak detection, under-slab and underground water service leaks, repairs, and reroutes. Leak detection by acoustical, Thermal, or tracer gas , methods.Also emphasize advanced drain cleaning technologies and equipment. Don't just poke ahole in the drain blockage, Clean the pipe, with our High pressure hydrojetters, or Chain knocker drain cables that expand to the width of the pipe being cleaned.

Number of Pages Required

5+ page

Font styles to use
Sans Serif

Requirements
Should not have
• Canned photos

```html
<!DOCTYPE html>
<html lang="en">
<head>
<meta charset="utf-8">
<title>Drainwise Plumbing</title>
<link rel="stylesheet" href="https://fonts.googleapis.com/css2?family=Montserrat:wght@600;700;800&family=Mulish:wght@400;600;700&display=swap">
<style>
:root{
  --black:#121212;
  --footer:#141414;
  --blue:#1565b5;
  --blue-dark:#0d4f9c;
  --blue-light:#1a8ad8;
  --sky:#25a8e8;
  --text:#555;
  --muted:#777;
  --white:#fff;
}
*{margin:0;padding:0;box-sizing:border-box}
html,body{width:1200px;height:3120px;overflow:hidden}
body{font-family:'Mulish',sans-serif;color:var(--text);background:var(--white);position:relative}
section,header,footer{position:relative;width:1200px}
.abs{position:absolute}

/* header */
.site-header{height:92px;background:var(--black)}
.brand{left:75px;top:26px;display:flex;align-items:center;gap:10px;color:var(--white);font-family:'Montserrat',sans-serif;font-weight:700;font-size:24px;letter-spacing:.5px}
.brand-dot{width:22px;height:22px;border-radius:50%;background:var(--sky)}
.main-nav{right:80px;top:36px;display:flex;gap:29px;font-size:14px;color:var(--white);letter-spacing:.3px}
.main-nav .active{color:var(--sky)}

/* hero */
.hero{height:555px;overflow:hidden}
.hero-photo{inset:0;background:linear-gradient(100deg,#c9ccd0 0%,#e6e7e9 25%,#a7adb5 45%,#5d6f8e 60%,#2a4a86 78%,#1f3c78 100%)}
.hero-circle{left:649px;top:126px;width:354px;height:354px;border-radius:50%;background:linear-gradient(160deg,#1a6fc4 0%,#1c56aa 55%,#2a3f95 100%);color:var(--white);text-align:center}
.hero-title{position:absolute;left:0;right:0;top:120px;font-family:'Montserrat',sans-serif;font-weight:700;font-size:36px;letter-spacing:.5px}
.hero-text{position:absolute;left:40px;right:40px;top:172px;font-size:17px;line-height:28px}
.hero-arrow{left:950px;top:449px;width:61px;height:61px;border-radius:50%;background:#0b0b0b}

/* welcome */
.welcome{height:596px}
.welcome-accent{left:200px;top:83px;width:294px;height:310px;background:var(--blue)}
.welcome-photo{left:77px;top:103px;width:396px;height:398px;background:linear-gradient(135deg,#8a8376 0%,#b6b0a4 40%,#d9d6d1 60%,#6b6452 100%)}
.section-heading{font-family:'Montserrat',sans-serif;font-weight:700;font-size:40px;color:var(--blue-dark);letter-spacing:.5px}
.section-heading .tint{color:var(--blue-light)}
.welcome-heading{left:607px;top:118px;width:480px;line-height:48px}
.welcome-copy{left:607px;top:234px;width:520px;font-size:13.5px;line-height:25px;color:var(--muted)}
.welcome-copy p+p{margin-top:12px}
.text-link{display:flex;align-items:center;gap:12px;font-family:'Montserrat',sans-serif;font-weight:700;font-size:13px;color:var(--blue);letter-spacing:.6px;text-decoration:underline;text-underline-offset:4px}
.welcome .text-link{left:607px;top:462px}

/* services */
.services{height:552px;background:var(--black)}
.services .section-heading{left:0;right:0;top:46px;text-align:center}
.service-card{top:119px;width:323px}
.service-photo{height:230px}
.service-bar{height:71px;background:var(--blue);display:flex;align-items:center;justify-content:space-between;padding:0 22px 0 24px;color:var(--white);font-size:19px}
.services .text-link{left:0;right:0;top:458px;justify-content:center;color:var(--sky)}

/* testimonials */
.testimonials{height:500px;overflow:hidden;background:linear-gradient(100deg,#1ca4e4 0%,#1a84d2 45%,#1b5cb6 75%,#2048a8 100%)}
.testimonials .section-heading{left:0;right:0;top:46px;text-align:center;color:var(--white)}
.quote-box{left:267px;top:163px;width:666px;height:175px;background:rgba(255,255,255,.14);text-align:center;color:var(--white)}
.avatar{left:560px;top:122px;width:80px;height:80px;border-radius:50%;background:linear-gradient(135deg,#c9b8a8,#6d5a4d);border:3px solid var(--white)}
.client-name{position:absolute;left:0;right:0;top:70px;font-size:20px;font-weight:700}
.quote{position:absolute;left:36px;right:36px;top:108px;font-size:13.5px;line-height:25px}
.dots{left:0;right:0;top:414px;display:flex;justify-content:center;gap:4px}
.dots span{width:11px;height:11px;border-radius:50%;border:1.5px solid var(--white)}
.dots span.on{background:var(--white)}

/* news */
.news{height:650px}
.news .section-heading{left:0;right:0;top:46px;text-align:center}
.news-card{top:120px;width:323px}
.news-photo{height:218px;border-radius:4px}
.news-date{position:absolute;top:170px;right:18px;width:84px;height:84px;border-radius:50%;background:var(--blue);color:var(--white);text-align:center;border:3px solid var(--white)}
.news-date b{display:block;margin-top:14px;font-size:26px;font-weight:600;font-family:'Montserrat',sans-serif}
.news-date small{display:block;font-size:12px;margin-top:0}
.posted{margin-top:38px;font-size:14px;color:var(--blue);letter-spacing:.3px}
.news-title{margin-top:12px;font-size:18px;line-height:28px;font-weight:700;color:#222;font-family:'Mulish',sans-serif}
.news-text{margin-top:14px;font-size:13px;line-height:25px;color:var(--muted)}

/* footer */
.contact-strip{height:103px;background:var(--footer);display:flex;border-bottom:1px solid #333}
.contact-item{flex:1;display:flex;align-items:flex-start;gap:16px;padding:32px 0 0;color:var(--white);font-size:13.5px;line-height:25px}
.contact-item+.contact-item{border-left:1px solid #333}
.contact-item:nth-child(1){padding-left:120px}
.contact-item:nth-child(2){padding-left:112px}
.contact-item:nth-child(3){padding-left:86px}
.contact-item svg{margin-top:5px;flex:none}
.copyright{height:72px;background:var(--footer);text-align:center;color:#ccc;font-size:13px;line-height:72px;letter-spacing:.3px}
</style>
</head>
<body>

<header class="site-header">
  <div class="brand abs"><span class="brand-dot"></span>Drainwise</div>
  <nav class="main-nav abs">
    <span class="active">HOME</span><span>ABOUT</span><span>SERVICES</span><span>TESTIMONIALS</span><span>NEWS</span><span>CONTACT</span>
  </nav>
</header>

<section class="hero">
  <div class="hero-photo abs" role="img" aria-label="Plumber tightening a chrome sink trap with a wrench"></div>
  <div class="hero-circle abs">
    <h1 class="hero-title">DRAINWISE</h1>
    <p class="hero-text">Lorem Ipsum is simply dummy text of the printing and typesetting.</p>
  </div>
  <div class="hero-arrow abs">
    <svg width="61" height="61" viewBox="0 0 61 61"><path d="M19 30.5h22M33 22l9 8.5-9 8.5" fill="none" stroke="#fff" stroke-width="3" stroke-linecap="round" stroke-linejoin="round"/></svg>
  </div>
</section>

<section class="welcome">
  <div class="welcome-accent abs"></div>
  <div class="welcome-photo abs" role="img" aria-label="Plumber crouching beside a pipe with a hose in a crawl space"></div>
  <h2 class="section-heading welcome-heading abs"><span class="tint">WELCOME TO</span> DRAINWISE</h2>
  <div class="welcome-copy abs">
    <p>Lorem Ipsum is simply dummy text of the printing and typesetting industry. Lorem Ipsum has been the industry's standard dummy text ever since the 1500s, when an unknown printer took a galley of type and scrambled it to make a type specimen book. It has survived not only five centuries, but also the leap into electronic typesetting, remaining essentially unchanged.</p>
    <p>It was popularised in the 1960s with the release of Letraset sheets containing Lorem Ipsum passages, and more recently with desktop publishing software like Aldus PageMaker including versions of Lorem Ipsum.</p>
  </div>
  <div class="text-link abs">KNOW MORE
    <svg width="18" height="12" viewBox="0 0 18 12"><path d="M1 6h15M11 1l5 5-5 5" fill="none" stroke="currentColor" stroke-width="1.6"/></svg>
  </div>
</section>

<section class="services">
  <h2 class="section-heading abs"><span class="tint">SERVICES</span> WE PROVIDE</h2>
  <div class="service-card abs" style="left:77px">
    <div class="service-photo" role="img" aria-label="Drain cleaning under a sink with a cable machine" style="background:linear-gradient(135deg,#c9b27a,#e8e4dc 45%,#8a6a4a)"></div>
    <div class="service-bar">Drain cleaning<svg width="36" height="36" viewBox="0 0 36 36"><circle cx="18" cy="18" r="17" fill="#fff"/><path d="M10 18h15M19 11l7 7-7 7" fill="none" stroke="#1565b5" stroke-width="3.2" stroke-linecap="round" stroke-linejoin="round"/></svg></div>
  </div>
  <div class="service-card abs" style="left:438px">
    <div class="service-photo" role="img" aria-label="Technician testing for leaks on a flat roof" style="background:linear-gradient(180deg,#b8c8dc 0%,#d8dde4 40%,#8a8f96 60%,#6e7378 100%)"></div>
    <div class="service-bar">Leak detection<svg width="36" height="36" viewBox="0 0 36 36"><circle cx="18" cy="18" r="17" fill="#fff"/><path d="M10 18h15M19 11l7 7-7 7" fill="none" stroke="#1565b5" stroke-width="3.2" stroke-linecap="round" stroke-linejoin="round"/></svg></div>
  </div>
  <div class="service-card abs" style="left:800px">
    <div class="service-photo" role="img" aria-label="Plumber repairing a sink trap with a wrench" style="background:linear-gradient(120deg,#c8ccd2,#e4e5e7 40%,#3a5c9a 75%,#22407a)"></div>
    <div class="service-bar">Repairs<svg width="36" height="36" viewBox="0 0 36 36"><circle cx="18" cy="18" r="17" fill="#fff"/><path d="M10 18h15M19 11l7 7-7 7" fill="none" stroke="#1565b5" stroke-width="3.2" stroke-linecap="round" stroke-linejoin="round"/></svg></div>
  </div>
  <div class="text-link abs">EXPLORE MORE
    <svg width="18" height="12" viewBox="0 0 18 12"><path d="M1 6h15M11 1l5 5-5 5" fill="none" stroke="currentColor" stroke-width="1.6"/></svg>
  </div>
</section>

<section class="testimonials">
  <h2 class="section-heading abs">CLIENT TESTIMONIALS</h2>
  <div class="quote-box abs">
    <p class="client-name">- Client Name</p>
    <p class="quote">Lorem Ipsum is simply dummy text of the printing and typesetting industry. Lorem Ipsum has been the industry's standard dummy text ever since the 1500s, when an unknown printer took a galley of type and scrambled it to make a type specimen book.</p>
  </div>
  <div class="avatar abs" role="img" aria-label="Client portrait"></div>
  <div class="dots abs"><span class="on"></span><span></span><span></span><span></span></div>
</section>

<section class="news">
  <h2 class="section-heading abs">LATEST NEWS</h2>
  <article class="news-card abs" style="left:77px">
    <div class="news-photo" role="img" aria-label="Wrench on a pipe under a white basin" style="background:linear-gradient(135deg,#e6e6e6,#bfc3c8 50%,#8d9298)"></div>
    <div class="news-date"><b>20</b><small>MAR</small></div>
    <p class="posted">POSTED BY ADMIN</p>
    <h3 class="news-title">Lorem Ipsum is simply dummy text of the printing and typesetting.</h3>
    <p class="news-text">Lorem Ipsum is simply dummy text of the printing and typesetting industry. Lorem Ipsum has been the industry's standard dummy text ever since the 1500s, when an unknown printer took a galley.</p>
  </article>
  <article class="news-card abs" style="left:438px">
    <div class="news-photo" role="img" aria-label="Gloved hands fitting a valve with a wrench" style="background:linear-gradient(135deg,#2b2b2b,#6a3a2a 45%,#c4472b 70%,#3a3a3a)"></div>
    <div class="news-date"><b>20</b><small>MAR</small></div>
    <p class="posted">POSTED BY ADMIN</p>
    <h3 class="news-title">Lorem Ipsum is simply dummy text of the printing and typesetting.</h3>
    <p class="news-text">Lorem Ipsum is simply dummy text of the printing and typesetting industry. Lorem Ipsum has been the industry's standard dummy text ever since the 1500s, when an unknown printer took a galley.</p>
  </article>
  <article class="news-card abs" style="left:800px">
    <div class="news-photo" role="img" aria-label="Plumber in overalls standing beside a water heater" style="background:linear-gradient(135deg,#dfe3e8,#f2f2f2 40%,#3d63a8 65%,#c9ced6)"></div>
    <div class="news-date"><b>20</b><small>MAR</small></div>
    <p class="posted">POSTED BY ADMIN</p>
    <h3 class="news-title">Lorem Ipsum is simply dummy text of the printing and typesetting.</h3>
    <p class="news-text">Lorem Ipsum is simply dummy text of the printing and typesetting industry. Lorem Ipsum has been the industry's standard dummy text ever since the 1500s, when an unknown printer took a galley.</p>
  </article>
</section>

<footer>
  <div class="contact-strip">
    <div class="contact-item">
      <svg width="16" height="22" viewBox="0 0 16 22"><path d="M8 0C3.6 0 0 3.5 0 7.9 0 13.5 8 22 8 22s8-8.5 8-14.1C16 3.5 12.4 0 8 0z" fill="#25a8e8"/><circle cx="8" cy="8" r="3" fill="#141414"/></svg>
      <p>Lorem Ipsum is simply dummy<br>text of the printing.</p>
    </div>
    <div class="contact-item">
      <svg width="20" height="20" viewBox="0 0 24 24"><path d="M6.6 10.8a15.2 15.2 0 0 0 6.6 6.6l2.2-2.2c.3-.3.7-.4 1-.2 1.1.4 2.3.6 3.6.6.6 0 1 .4 1 1V20c0 .6-.4 1-1 1A17 17 0 0 1 3 4c0-.6.4-1 1-1h3.5c.6 0 1 .4 1 1 0 1.3.2 2.5.6 3.6.1.3 0 .7-.2 1z" fill="#25a8e8"/></svg>
      <p>CALL US:<br>555 014 2290</p>
    </div>
    <div class="contact-item">
      <svg width="20" height="15" viewBox="0 0 20 15"><rect x="0" y="0" width="20" height="15" rx="1.5" fill="#25a8e8"/><path d="M1 1.5l9 7 9-7" fill="none" stroke="#141414" stroke-width="1.6"/></svg>
      <p>EMAIL US:<br>info@drainwise-plumbing.com</p>
    </div>
  </div>
  <div class="copyright">©DRAINWISE PLUMBING. 2019 - All Rights Reserved.</div>
</footer>

</body>
</html>
```